TillHarbor Flyer

Create a flyer that is smart / business looking to advertise our Point Of Sale Software.

Further info can be obtained from www.tillharbor-demo.com.au

Other info:
www.tillharbor-demo.com.au
admin@tillharbor-demo.com.au
PH: 1300 462 097

Target Market(s)

Business Owners , point of sale for business

Industry/Entity Type

Business

Colors

Designer to choose colors to be used in the design.

Requirements
Nice to have
• Perfer Company Colours
• www.tillharbor-demo.com.au
• but more important to look good
• More information can be found on our website

```html
<!DOCTYPE html>
<html lang="en">
<head>
<meta charset="utf-8">
<title>TillHarbor Flyer</title>
<link href="https://fonts.googleapis.com/css2?family=Roboto:wght@400;500;700&display=swap" rel="stylesheet">
<style>
  :root {
    --red: #e23232;
    --ink: #4a4a4a;
    --grey: #7a7a7a;
    --page-bg: #e9e9ea;
    --paper: #ffffff;
    --photo-dark: #1d2a3c;
    --photo-mid: #4a5d78;
    --photo-light: #c9b9ad;
  }
  * { box-sizing: border-box; margin: 0; padding: 0; }
  html, body { width: 1038px; height: 1200px; overflow: hidden; }
  body { background: var(--page-bg); font-family: 'Roboto', sans-serif; }

  .flyer {
    position: absolute; left: 91px; top: 20px;
    width: 856px; height: 1160px;
    background: var(--paper);
    box-shadow: 0 2px 10px rgba(0,0,0,.12);
  }
  .abs { position: absolute; }

  .header-bar { left: 16px; top: 19px; width: 8px; height: 78px; background: var(--red); }
  .header-line { left: 16px; top: 19px; width: 311px; height: 5px; background: var(--red); }
  .brand { left: 34px; top: 38px; display: flex; align-items: center; gap: 10px; }
  .brand-dot { width: 34px; height: 34px; border-radius: 50%; background: var(--red); }
  .brand-name { font-size: 40px; font-weight: 500; color: var(--ink); line-height: 1; }
  .brand-tag { left: 230px; top: 82px; font-size: 10px; color: var(--ink); }
  .site-url { right: 14px; top: 50px; font-size: 20px; color: var(--grey); }

  .hero-photo {
    left: 16px; top: 118px; width: 826px; height: 356px;
    background: linear-gradient(100deg, var(--photo-dark) 0%, var(--photo-mid) 45%, var(--photo-light) 70%, var(--photo-dark) 100%);
  }

  .section-title { left: 470px; top: 522px; font-size: 25px; font-weight: 700; color: var(--ink); }

  .service {
    left: 470px; width: 373px; height: 143px;
    background: var(--red); color: #fff; padding: 12px 16px 0 16px;
  }
  .service-head { display: flex; align-items: center; gap: 10px; font-size: 22px; font-weight: 500; margin-bottom: 8px; }
  .service-icon { width: 20px; height: 20px; }
  .service p { font-size: 14.5px; line-height: 17.5px; text-align: justify; }

  .label-box {
    left: 31px; width: 228px; height: 54px;
    border: 2px solid var(--red); color: var(--ink);
    font-size: 24px; font-weight: 500;
    display: flex; align-items: center; justify-content: center; letter-spacing: .5px;
  }
  .copy { left: 31px; width: 392px; font-size: 13px; line-height: 20px; color: var(--grey); text-align: justify; }
  .copy p + p { margin-top: 20px; }

  .footer { left: 16px; top: 1061px; width: 826px; height: 68px; background: var(--red); }
  .phone-box {
    position: absolute; left: 26px; top: 11px; width: 211px; height: 47px;
    border: 2px solid #fff; color: #fff; font-size: 21px;
    display: flex; align-items: center; gap: 14px; padding-left: 12px;
  }
  .address {
    position: absolute; right: 34px; top: 0; height: 68px; color: #fff; font-size: 18px;
    display: flex; align-items: center; gap: 14px;
  }
</style>
</head>
<body>
<div class="flyer">
  <div class="abs header-bar"></div>
  <div class="abs header-line"></div>
  <div class="abs brand"><span class="brand-dot"></span><span class="brand-name">TillHarbor</span></div>
  <div class="abs brand-tag">powered by Quayline</div>
  <div class="abs site-url">www.tillharbor-demo.com.au</div>

  <div class="abs hero-photo" role="img" aria-label="Photo of a businessman in a suit touching a glowing network of connected circles, with a red faceted accent at the lower left"></div>

  <div class="abs section-title">OUR SERVICES</div>

  <div class="abs service" style="top:570px">
    <div class="service-head">
      <svg class="service-icon" viewBox="0 0 20 20"><circle cx="10" cy="10" r="8.5" fill="none" stroke="#fff" stroke-width="2"/><circle cx="10" cy="10" r="4" fill="#fff"/></svg>
      POINT OF SALE
    </div>
    <p>TillHarbor is your complete Point of Sale software. It's classy design and easy functionality makes it a breeze for all staff to use. Easy payment options make the sale process flawless and quick.</p>
  </div>
  <div class="abs service" style="top:729px">
    <div class="service-head">
      <svg class="service-icon" viewBox="0 0 20 20"><circle cx="10" cy="10" r="8.5" fill="none" stroke="#fff" stroke-width="2"/><circle cx="10" cy="10" r="4" fill="#fff"/></svg>
      BUSINESS ANALYSIS
    </div>
    <p>TillHarbor automatically takes all your Point of Sale data and collates it into reports for you. You can customise reports so you get the data you need to successfully manage your business on the fly.</p>
  </div>
  <div class="abs service" style="top:888px">
    <div class="service-head">
      <svg class="service-icon" viewBox="0 0 20 20"><circle cx="10" cy="10" r="8.5" fill="none" stroke="#fff" stroke-width="2"/><circle cx="10" cy="10" r="4" fill="#fff"/></svg>
      SUPPORT
    </div>
    <p>Your TillHarbor subscription comes with full back up and support. We have online support, telephone support, email support and also onsite support if required. Try before you buy here:</p>
  </div>

  <div class="abs label-box" style="top:603px">WHO WE ARE ?</div>
  <div class="abs copy" style="top:680px">
    <p>TillHarbor was derived back in 2014 when two business men found the need for a single software package to not only do all the Point Of Sale tasks for their business but also to have this data transfered into reports for managing their business.</p>
    <p>TillHarbor will track all your business activities from Sales, Purchases, Expenses, GST, Stock Control, Warehousing etc for single to multi-store businesses.</p>
  </div>

  <div class="abs label-box" style="top:878px">WHAT WE DO ?</div>
  <div class="abs copy" style="top:957px">
    <p>TillHarbor tracks all aspects of your business in the one software package. Sales, Purchasing, Expenses, GST and collates all this information into an extensive range of reports.</p>
  </div>

  <div class="abs footer">
    <div class="phone-box">
      <svg width="24" height="24" viewBox="0 0 24 24"><path fill="#fff" d="M6.6 10.8a15.1 15.1 0 0 0 6.6 6.6l2.2-2.2a1 1 0 0 1 1-.25 11.4 11.4 0 0 0 3.6.57 1 1 0 0 1 1 1V20a1 1 0 0 1-1 1A17 17 0 0 1 3 4a1 1 0 0 1 1-1h3.5a1 1 0 0 1 1 1c0 1.250.2 2.450.57 3.570a1 1 0 0 1-.25 1z"/></svg>
      +1300 462 097
    </div>
    <div class="address">
      <svg width="26" height="24" viewBox="0 0 26 24"><path fill="none" stroke="#fff" stroke-width="2" stroke-linejoin="round" d="M1 4l7-3 10 3 7-3v19l-7 3-10-3-7 3z M8 1v19 M18 4v19"/></svg>
      48 Wharf Lane, RIVERTON VIC 3999
    </div>
  </div>
</div>
</body>
</html>
```